Sunny Trails and joy Business card

I have a logo, but will like a business card design. Is for a travel agency in Mexico. We focus in family experiences.

I will liek some thing different and unique, from the traditional business card, something to get remmeber for.

Business card information:

Leandro R. Quiroga
leandro@sunnytrailsjoy.example

Alameda 742, 3 piso
Col. Tepalcatl
Mexico, D.F. 04910

office: (55) 4821-7390
mobile: (55) 7034-1258

www.sunnytrailsjoy.example
@sunnytjoy
blog: sunnytrailsandjoy.blog.example
facebook: SunnyTrailsAndJoy

```html
<!DOCTYPE html>
<html lang="en">
<head>
<meta charset="utf-8">
<title>Sunny Trails and joy – Business Card</title>
<link rel="stylesheet" href="https://fonts.googleapis.com/css2?family=Source+Sans+3:wght@400;600;700&display=swap">
<style>
  :root {
    --brand-blue: #10558a;
    --sky-light: #cfe6f5;
    --stripe-blue: #6fa6dc;
    --paper: #ffffff;
    --ink-grey: #4a4a4a;
    --page-bg: #ffffff;
  }
  * { box-sizing: border-box; margin: 0; padding: 0; }
  html, body {
    width: 1200px; height: 900px; overflow: hidden;
    background: var(--page-bg);
    font-family: "Source Sans 3", "Myriad Pro", Arial, sans-serif;
  }
  .canvas { position: relative; width: 1200px; height: 900px; }

  .card {
    position: absolute; left: 273px; width: 642px; height: 367px;
    border-radius: 22px; overflow: hidden;
    box-shadow: 3px 5px 8px rgba(0,0,0,.35);
  }

  /* Front */
  .card--front { top: 48px; background: var(--brand-blue); }
  .front-mark-circle {
    position: absolute; left: 262px; top: 62px; width: 120px; height: 120px;
    border-radius: 50%; background: var(--sky-light);
  }
  .front-brand-name {
    position: absolute; left: 0; right: 0; top: 196px;
    text-align: center; color: var(--paper);
    font-weight: 700; font-size: 44px; line-height: 1;
  }
  .front-url {
    position: absolute; left: 0; right: 0; top: 326px;
    text-align: center; color: var(--paper); font-size: 19px;
  }
  .front-url strong { font-weight: 700; }

  /* Back */
  .card--back { top: 485px; background: var(--paper); }
  .back-top { position: absolute; left: 0; top: 0; width: 100%; height: 215px; background: var(--paper); }
  .back-stripe { position: absolute; left: 0; top: 215px; width: 100%; height: 9px; background: var(--stripe-blue); }
  .back-bottom { position: absolute; left: 0; top: 224px; width: 100%; bottom: 0; background: var(--brand-blue); }

  .back-mark-circle {
    position: absolute; left: 78px; top: 32px; width: 84px; height: 84px;
    border-radius: 50%; background: var(--sky-light);
  }
  .back-brand-name {
    position: absolute; left: 36px; width: 260px; top: 120px;
    text-align: center; color: var(--brand-blue);
    font-weight: 700; font-size: 30px; line-height: 1.05;
  }

  .contact-person {
    position: absolute; right: 36px; top: 84px; text-align: right;
  }
  .person-name {
    color: var(--brand-blue); font-weight: 700; font-size: 21px; margin-bottom: 10px;
  }
  .contact-line, .social-line {
    display: flex; justify-content: flex-end; align-items: center; gap: 8px;
    font-size: 16px; line-height: 21.5px;
  }
  .contact-line { color: var(--ink-grey); }
  .icon { width: 13px; height: 13px; flex: none; }
  .icon--blue { fill: var(--brand-blue); }
  .icon--white { fill: var(--paper); }

  .office-address {
    position: absolute; left: 45px; top: 271px;
    color: var(--paper); font-size: 16px; line-height: 21.5px; font-style: normal;
  }
  .social-list {
    position: absolute; right: 36px; top: 249px; color: var(--paper);
  }
</style>
</head>
<body>
<div class="canvas">

  <section class="card card--front">
    <div class="front-mark-circle"></div>
    <div class="front-brand-name">Sunny Trails<br>and joy</div>
    <div class="front-url">www.<strong>sunnytrailsjoy</strong>.example</div>
  </section>

  <section class="card card--back">
    <div class="back-top"></div>
    <div class="back-stripe"></div>
    <div class="back-bottom"></div>

    <div class="back-mark-circle"></div>
    <div class="back-brand-name">Sunny Trails<br>and joy</div>

    <div class="contact-person">
      <div class="person-name">Leandro R. Quiroga</div>
      <div class="contact-line">(55) 4821-7390
        <svg class="icon icon--blue" viewBox="0 0 16 16"><path d="M3 1l3 3-1.5 2a9 9 0 0 0 5.5 5.5L12 10l3 3-2 2C7 15 1 9 1 3z"/></svg>
      </div>
      <div class="contact-line">(55) 7034-1258
        <svg class="icon icon--blue" viewBox="0 0 16 16"><path d="M4 0h8v16H4zM5.5 2v10h5V2z"/><circle cx="8" cy="14" r="1" fill="#fff"/></svg>
      </div>
      <div class="contact-line">leandro@sunnytrailsjoy.example
        <svg class="icon icon--blue" viewBox="0 0 16 16"><path d="M1 3h14v10H1z"/><path d="M1 3l7 6 7-6" stroke="#fff" stroke-width="1.4" fill="none"/></svg>
      </div>
    </div>

    <address class="office-address">
      Alameda 742, 3 piso<br>
      Col. Tepalcatl<br>
      Mexico, D.F. 04910
    </address>

    <div class="social-list">
      <div class="social-line">@sunnytjoy
        <svg class="icon icon--white" viewBox="0 0 16 16"><circle cx="8" cy="8" r="7"/></svg>
      </div>
      <div class="social-line">sunnytrailsandjoy.blog.example
        <svg class="icon icon--white" viewBox="0 0 16 16"><circle cx="8" cy="8" r="7"/></svg>
      </div>
      <div class="social-line">SunnyTrailsAndJoy
        <svg class="icon icon--white" viewBox="0 0 16 16"><circle cx="8" cy="8" r="7"/></svg>
      </div>
      <div class="social-line">www.sunnytrailsjoy.example
        <svg class="icon icon--white" viewBox="0 0 16 16"><circle cx="8" cy="8" r="7"/><path d="M1 8h14M8 1c-3 3-3 11 0 14M8 1c3 3 3 11 0 14" stroke="#10558a" stroke-width="1" fill="none"/></svg>
      </div>
    </div>
  </section>

</div>
</body>
</html>
```